Design a Mobile App for Landscape Businesses

This project is to design the first three screens for a mobile app for Landscape and Lawncare businesses. This app will serve as a directory for homeowners to locate landscape and lawn care businesses and for landscape businesses and contractors to run their business. See the attached PDF for more information and example
Here is the link to the description https://brevlinq.test/k3r92P

Target Market(s)

Landscape and lawn care business, gardeners, home owners

Industry/Entity Type

Landscape Gardening

Logo Text

Quillmoray

Colors

Designer to choose colors to be used in the design.

```html
<!DOCTYPE html>
<html lang="en">
<head>
<meta charset="utf-8">
<title>Find a Gardener</title>
<link href="https://fonts.googleapis.com/css2?family=Montserrat:wght@400;500;600;700&display=swap" rel="stylesheet">
<style>
:root{
  --green:#3aa935;
  --green-dark:#2e8f2b;
  --ink:#1f2a30;
  --text:#4a5257;
  --muted:#8a9196;
  --line:#e3e6e8;
  --bg:#ffffff;
  --map-a:#e9eaeb;
  --map-b:#dfe8d9;
  --water:#b9dcf0;
  --alert:#f26b21;
}
*{box-sizing:border-box;margin:0;padding:0}
html,body{width:675px;height:1200px;overflow:hidden;background:var(--bg)}
body{font-family:"Montserrat",sans-serif;color:var(--ink);position:relative}
.status-bar{position:absolute;top:0;left:0;width:675px;height:43px;display:flex;justify-content:flex-end;align-items:center;gap:10px;padding-right:22px;font-size:22px;color:var(--ink)}
.app-header{position:absolute;top:43px;left:0;width:675px;height:80px;display:flex;align-items:center;padding:0 24px;background:var(--bg)}
.app-title{font-size:26px;font-weight:700;flex:1}
.header-action{display:flex;align-items:center;gap:8px;color:var(--green);font-weight:600;font-size:22px;margin-left:34px}
.map-area{position:absolute;top:123px;left:0;width:675px;height:800px;background:linear-gradient(160deg,var(--map-b) 0%,var(--map-a) 30%,var(--water) 46%,var(--map-a) 52%,#efe9d8 78%,var(--map-a) 100%)}
.filter-bar{position:absolute;top:137px;left:11px;width:653px;height:76px;background:var(--bg);display:flex;border-radius:4px;box-shadow:0 2px 6px rgba(0,0,0,.15)}
.filter{flex:1;display:flex;align-items:center;gap:10px;padding:0 16px;font-size:22px;font-weight:600}
.filter + .filter{border-left:2px solid var(--line)}
.filter .label{flex:1;white-space:nowrap}
.filter .light{font-weight:500}
.pin{position:absolute;display:flex;flex-direction:column;align-items:center}
.pin-tag{background:var(--green);color:#fff;font-weight:700;border:4px solid #fff;border-radius:4px;box-shadow:0 2px 4px rgba(0,0,0,.25);display:flex;align-items:center;justify-content:center}
.pin-stem{width:4px;height:14px;background:#555}
.pin-shadow{width:34px;height:8px;border-radius:50%;background:rgba(0,0,0,.2);margin-top:-4px}
.pin-sm .pin-tag{width:62px;height:44px;font-size:20px}
.pin-lg .pin-tag{width:84px;height:54px;font-size:26px}
.detail-card{position:absolute;top:886px;left:0;width:675px;height:230px;background:var(--bg);border-radius:22px 22px 0 0;box-shadow:0 -3px 10px rgba(0,0,0,.12);padding:0 24px}
.handle{width:70px;height:7px;background:var(--line);border-radius:4px;margin:11px auto 0}
.business-name{font-size:31px;font-weight:700;margin-top:22px}
.business-row{display:flex;align-items:flex-start;margin-top:14px}
.business-desc{flex:1;font-size:22px;line-height:34px;color:var(--text);max-height:68px;overflow:hidden;display:-webkit-box;-webkit-line-clamp:2;-webkit-box-orient:vertical;padding-right:40px}
.quote-link{display:flex;align-items:center;gap:10px;color:var(--green);font-weight:700;font-size:23px;margin-top:14px}
.phone{display:flex;align-items:center;gap:14px;font-size:23px;margin-top:14px;color:var(--ink)}
.tab-bar{position:absolute;top:1116px;left:0;width:675px;height:84px;border-top:2px solid var(--line);display:flex;background:var(--bg)}
.tab{flex:1;display:flex;flex-direction:column;align-items:center;justify-content:center;gap:6px;font-size:18px;color:var(--muted);position:relative}
.tab.active{color:var(--green);font-weight:600}
.badge{position:absolute;top:14px;left:50%;margin-left:10px;width:14px;height:14px;border-radius:50%;background:var(--alert)}
</style>
</head>
<body>
<div class="status-bar">
  <svg width="22" height="22" viewBox="0 0 24 24"><circle cx="12" cy="13" r="8" fill="none" stroke="#1f2a30" stroke-width="2.4"/><path d="M12 9v4l3 2" stroke="#1f2a30" stroke-width="2.4" fill="none"/></svg>
  <svg width="24" height="22" viewBox="0 0 24 20"><path d="M12 19L0 5a18 18 0 0 1 24 0z" fill="#1f2a30"/></svg>
  <svg width="22" height="22" viewBox="0 0 22 22"><path d="M22 0v22H0z" fill="#1f2a30"/></svg>
  <svg width="14" height="24" viewBox="0 0 14 24"><rect x="4" y="0" width="6" height="3" fill="#1f2a30"/><rect x="0" y="3" width="14" height="21" rx="2" fill="#1f2a30"/></svg>
  <span>16:54</span>
</div>

<header class="app-header">
  <h1 class="app-title">Find a Gardener</h1>
  <div class="header-action">
    <svg width="22" height="22" viewBox="0 0 24 24"><path d="M2 3h20l-8 9v8l-4 2V12z" fill="none" stroke="#3aa935" stroke-width="2.2" stroke-linejoin="round"/></svg>Filter
  </div>
  <div class="header-action">
    <svg width="24" height="22" viewBox="0 0 24 22"><g fill="#3aa935"><rect x="0" y="2" width="4" height="3"/><rect x="7" y="2" width="17" height="3"/><rect x="0" y="9" width="4" height="3"/><rect x="7" y="9" width="17" height="3"/><rect x="0" y="16" width="4" height="3"/><rect x="7" y="16" width="17" height="3"/></g></svg>List
  </div>
</header>

<div class="map-area" role="img" aria-label="Street map of the city centre showing the river, parks and nearby gardeners"></div>

<div class="filter-bar">
  <div class="filter">
    <svg width="20" height="26" viewBox="0 0 20 26"><path d="M10 0a10 10 0 0 1 10 10c0 7-10 16-10 16S0 17 0 10A10 10 0 0 1 10 0z" fill="#3aa935"/><circle cx="10" cy="10" r="3.5" fill="#fff"/></svg>
    <span class="label">Current Location</span>
    <svg width="18" height="12" viewBox="0 0 18 12"><path d="M2 2l7 7 7-7" fill="none" stroke="#1f2a30" stroke-width="2.4"/></svg>
  </div>
  <div class="filter">
    <svg width="26" height="26" viewBox="0 0 26 26"><circle cx="13" cy="13" r="11" fill="none" stroke="#3aa935" stroke-width="2.4"/><path d="M13 7v6l4 3" fill="none" stroke="#3aa935" stroke-width="2.4"/></svg>
    <span class="label"><span class="light">Available:</span> Anytime</span>
    <svg width="18" height="12" viewBox="0 0 18 12"><path d="M2 2l7 7 7-7" fill="none" stroke="#1f2a30" stroke-width="2.4"/></svg>
  </div>
</div>

<div class="pin pin-sm" style="left:93px;top:307px"><div class="pin-tag">AG</div><div class="pin-stem"></div><div class="pin-shadow"></div></div>
<div class="pin pin-lg" style="left:291px;top:520px"><div class="pin-tag">HG</div><div class="pin-stem"></div><div class="pin-shadow"></div></div>
<div class="pin pin-sm" style="left:522px;top:598px"><div class="pin-tag">AB</div><div class="pin-stem"></div><div class="pin-shadow"></div></div>
<div class="pin pin-sm" style="left:27px;top:738px"><div class="pin-tag">WG</div><div class="pin-stem"></div><div class="pin-shadow"></div></div>
<div class="pin pin-sm" style="left:644px;top:336px"><div class="pin-tag">A</div><div class="pin-stem"></div><div class="pin-shadow"></div></div>

<section class="detail-card">
  <div class="handle"></div>
  <h2 class="business-name">Hollis Groundworks</h2>
  <div class="business-row">
    <p class="business-desc">Experienced and skilled gardener based in Scarborough. I specialise in lawn care, hedge trimming and planting.</p>
    <div class="quote-link">Quote
      <svg width="14" height="26" viewBox="0 0 14 26"><path d="M2 2l10 11L2 24" fill="none" stroke="#3aa935" stroke-width="2.6"/></svg>
    </div>
  </div>
  <div class="phone">
    <svg width="18" height="28" viewBox="0 0 18 28"><rect x="1.5" y="1.5" width="15" height="25" rx="3" fill="none" stroke="#3aa935" stroke-width="2.6"/><rect x="6" y="21" width="6" height="2" fill="#3aa935"/></svg>
    07700 900 482
  </div>
</section>

<nav class="tab-bar">
  <div class="tab active">
    <svg width="34" height="30" viewBox="0 0 34 30"><path d="M9 0a8 8 0 0 1 8 8c0 6-8 13-8 13S1 14 1 8a8 8 0 0 1 8-8z" fill="#3aa935"/><circle cx="9" cy="8" r="3" fill="#fff"/><path d="M25 8a8 8 0 0 1 8 8c0 6-8 13-8 13s-8-7-8-13a8 8 0 0 1 8-8z" fill="#3aa935"/><circle cx="25" cy="16" r="3" fill="#fff"/></svg>
    Search
  </div>
  <div class="tab">
    <svg width="28" height="28" viewBox="0 0 28 28"><g fill="none" stroke="#8a9196" stroke-width="2.4"><rect x="1.5" y="1.5" width="25" height="25" rx="2"/><path d="M6 8h3M12 8h10M6 14h3M12 14h10M6 20h3M12 20h10"/></g></svg>
    Bookings
  </div>
  <div class="tab">
    <span class="badge"></span>
    <svg width="32" height="24" viewBox="0 0 32 24"><g fill="none" stroke="#8a9196" stroke-width="2.4"><rect x="1.5" y="1.5" width="29" height="21" rx="2"/><path d="M2 3l14 11L30 3"/></g></svg>
    Messages
  </div>
  <div class="tab">
    <svg width="30" height="30" viewBox="0 0 30 30"><g fill="none" stroke="#8a9196" stroke-width="2.4"><circle cx="15" cy="15" r="5"/><path d="M15 2v5M15 23v5M2 15h5M23 15h5M5.8 5.8l3.5 3.5M20.7 20.7l3.5 3.5M5.8 24.2l3.5-3.5M20.7 9.3l3.5-3.5"/><circle cx="15" cy="15" r="10"/></g></svg>
    Account
  </div>
</nav>
</body>
</html>
```